One page, two sided flyer about our company needed for a conference

We are an IT consulting company and need a two sided flyer produced for our company that we are going to hand out to potential clients at a conference we have coming up.

We would like the design to be in-line with the look and feel of our current website design: www.brinvaroconsulting.example

Our logo has been attached along with some screenshots from our site that we would like included.

Target Market(s)

Business Executives

Industry/Entity Type

It Company

Font styles to use
Sans Serif

Colors
ec1f27

```html
<!DOCTYPE html>
<html lang="en">
<head>
<meta charset="utf-8">
<title>Brinvaro Consulting – Conference Flyer</title>
<link rel="stylesheet" href="https://fonts.googleapis.com/css2?family=Oswald:wght@400;500&family=Nunito:wght@300;400;600;700&display=swap">
<style>
  :root{
    --brand-red:#ec1f27;
    --deep-red:#8e1b1d;
    --charcoal:#1f2329;
    --charcoal-2:#2a2f36;
    --silver-1:#f1f1f2;
    --silver-2:#d6d7d9;
    --ink:#3a3a3c;
    --ink-soft:#555558;
    --white:#ffffff;
  }
  *{box-sizing:border-box;margin:0;padding:0}
  html,body{width:1200px;height:1000px;overflow:hidden;background:var(--white)}
  body{position:relative;font-family:"Nunito",sans-serif}

  .side{position:absolute;top:117px;width:547px;height:766px;overflow:hidden}
  .side--front{left:40px;background:radial-gradient(ellipse at 50% 50%,var(--silver-1) 0%,var(--silver-2) 100%)}
  .side--back{left:613px;background:var(--charcoal)}
  .side__shapes{position:absolute;inset:0}

  /* front */
  .brand-name{position:absolute;left:0;right:0;top:42px;text-align:center;color:var(--white);
    font-family:"Nunito",sans-serif;font-weight:700;font-size:30px;letter-spacing:2px;text-transform:uppercase}
  .front-title{position:absolute;left:0;right:0;top:180px;text-align:center;font-family:"Oswald",sans-serif;
    font-weight:400;font-size:42px;color:var(--ink)}
  .feature{position:absolute;left:26px;width:500px}
  .feature__tick{position:absolute;left:0;top:0;width:40px;height:40px}
  .feature__title{margin-left:56px;font-weight:300;font-size:17.5px;color:var(--ink);letter-spacing:.2px;padding-top:8px}
  .feature__text{margin-left:50px;margin-top:4px;font-weight:300;font-size:13px;line-height:19.5px;color:var(--ink-soft)}
  .front-footer{position:absolute;left:0;right:0;top:680px;text-align:center}
  .front-footer__title{font-family:"Oswald",sans-serif;font-size:19px;color:var(--brand-red)}
  .front-footer__text{font-size:10px;color:var(--white);margin-top:2px}

  /* back */
  .back-title{position:absolute;left:0;right:0;top:42px;text-align:center;font-family:"Oswald",sans-serif;
    font-size:44px;color:var(--white)}
  .accent{color:var(--brand-red)}
  .service__name{font-size:16px;color:var(--brand-red);font-weight:400}
  .service__text{font-size:12px;line-height:18px;color:var(--white);margin-top:6px}
  .service--managed{position:absolute;left:90px;width:370px;top:143px;text-align:center}
  .service--impl{position:absolute;left:25px;width:200px;top:278px}
  .service--virtual{position:absolute;left:344px;width:190px;top:278px}
  .service-icons{position:absolute;left:233px;top:246px;width:100px;height:115px}
  .overview-title{position:absolute;left:25px;top:403px;font-family:"Oswald",sans-serif;font-size:44px;color:var(--brand-red)}
  .overview-text{position:absolute;left:32px;top:470px;width:470px;font-size:16.5px;line-height:24px;color:var(--white)}
  .contact-band{position:absolute;left:0;top:609px;width:100%;height:157px;
    background:linear-gradient(90deg,var(--deep-red) 0%,#b3252a 45%,var(--deep-red) 100%)}
  .contact{position:absolute;left:36px;display:flex;align-items:center;gap:14px;color:var(--white);
    font-weight:700;font-size:12px}
  .contact svg{width:28px;height:28px}
  .band-brand{position:absolute;right:24px;top:60px;color:var(--white);font-weight:700;font-size:15px;
    letter-spacing:1px;text-transform:uppercase;text-align:center}
</style>
</head>
<body>

<section class="side side--front">
  <svg class="side__shapes" viewBox="0 0 547 766" aria-hidden="true">
    <polygon points="0,50 273,150 547,50 547,72 273,168 0,72" fill="#c9cacd"/>
    <polygon points="0,0 547,0 547,52 273,158 0,52" fill="var(--charcoal)"/>
    <polygon points="0,700 273,602 547,700 547,718 273,620 0,718" fill="#c9cacd"/>
    <polygon points="0,716 273,610 547,716 547,766 0,766" fill="var(--charcoal)"/>
  </svg>
  <div class="brand-name">Brinvaro Consulting</div>
  <h1 class="front-title">WHAT WE DO</h1>

  <div class="feature" style="top:242px">
    <svg class="feature__tick" viewBox="0 0 40 40"><circle cx="20" cy="20" r="18" fill="none" stroke="var(--brand-red)" stroke-width="2"/><path d="M12 20l6 6 11-11" fill="none" stroke="var(--brand-red)" stroke-width="3.5" stroke-linecap="round" stroke-linejoin="round"/></svg>
    <h2 class="feature__title">EXPERIENCED SOLUTION FOCUSED DEVELOPERS</h2>
    <p class="feature__text">All Of Our Developers Have Vast Amounts Of Experience In FlowDesk</p>
  </div>

  <div class="feature" style="top:360px">
    <svg class="feature__tick" viewBox="0 0 40 40"><circle cx="20" cy="20" r="18" fill="none" stroke="var(--brand-red)" stroke-width="2"/><path d="M12 20l6 6 11-11" fill="none" stroke="var(--brand-red)" stroke-width="3.5" stroke-linecap="round" stroke-linejoin="round"/></svg>
    <h2 class="feature__title">SUPERIOR SERVICE</h2>
    <p class="feature__text">Our Customers Come First And Our Client Retention Rate Of 98% Proves It. From Word One You Are Our Focus, Whether It Is Providing Alternative Solutions That No One Has Explored, Working With You On A Projects Price, Delivering A Finished Product By A Certain Date Etc.</p>
  </div>

  <div class="feature" style="top:514px">
    <svg class="feature__tick" viewBox="0 0 40 40"><circle cx="20" cy="20" r="18" fill="none" stroke="var(--brand-red)" stroke-width="2"/><path d="M12 20l6 6 11-11" fill="none" stroke="var(--brand-red)" stroke-width="3.5" stroke-linecap="round" stroke-linejoin="round"/></svg>
    <h2 class="feature__title">COMPETITIVE PRICING</h2>
    <p class="feature__text">All Solutions Are Presented With Several Delivery Options E.G Full-Time US Developers, A Hybrid Of US + Near Shore, Or All Near Shore.</p>
  </div>

  <div class="front-footer">
    <div class="front-footer__title">IT STRATEGY AND IMPLEMENTATION</div>
    <div class="front-footer__text">We take your company to the cutting edge of efficiency.</div>
  </div>
</section>

<section class="side side--back">
  <h1 class="back-title">OUR <span class="accent">SERVICES</span></h1>

  <div class="service service--managed">
    <h2 class="service__name">Managed Services</h2>
    <p class="service__text">The key to productivity and efficiency lies in doing only those things which need to be done. But, often companies end-up wasting time struggling with...</p>
  </div>

  <svg class="service-icons" viewBox="0 0 100 115" aria-hidden="true">
    <g fill="var(--white)" stroke="var(--brand-red)" stroke-width="2">
      <polygon points="50,2 74,15 74,42 50,55 26,42 26,15"/>
      <polygon points="26,58 50,71 50,98 26,111 2,98 2,71"/>
      <polygon points="74,58 98,71 98,98 74,111 50,98 50,71"/>
    </g>
    <g fill="var(--brand-red)">
      <rect x="42" y="18" width="16" height="11" rx="2"/>
      <path d="M40 40c0-8 4-12 10-12s10 4 10 12z"/>
      <rect x="17" y="78" width="18" height="12" rx="2" transform="rotate(-30 26 84)"/>
      <circle cx="66" cy="78" r="3"/><circle cx="74" cy="76" r="3"/><circle cx="82" cy="78" r="3"/>
      <rect x="63" y="83" width="6" height="12"/><rect x="71" y="81" width="6" height="14"/><rect x="79" y="83" width="6" height="12"/>
    </g>
  </svg>

  <div class="service service--impl">
    <h2 class="service__name">Implementation Services</h2>
    <p class="service__text">Starting from scratch is hard and resource-consuming with any system. That’s certainly the case with FlowDesk. You may have heard it can work wonders for...</p>
  </div>

  <div class="service service--virtual">
    <h2 class="service__name">Virtual Assistance</h2>
    <p class="service__text">FlowDesk is officially live for your team. The scope and initial deployment is done – your company is excited ...<br>Now what?&nbsp; Whether you need...</p>
  </div>

  <h2 class="overview-title">OVERVIEW</h2>
  <p class="overview-text">Brinvaro Consulting is a team of IT experts who command the IT field and its related software. From consultancy to implementation, we can help you identify the best solutions for your company and see them through to smooth, constant, and long-lasting operation.</p>

  <div class="contact-band">
    <div class="contact" style="top:16px">
      <svg viewBox="0 0 28 28"><rect x="2" y="6" width="24" height="16" fill="none" stroke="var(--white)" stroke-width="2"/><path d="M2 6l12 9 12-9" fill="none" stroke="var(--white)" stroke-width="2"/></svg>
      <span>info@brinvaroconsulting.example</span>
    </div>
    <div class="contact" style="top:64px">
      <svg viewBox="0 0 28 28"><path d="M6 3l5 5-3 3c2 4 5 7 9 9l3-3 5 5-4 4C11 25 3 17 2 7z" fill="var(--white)"/></svg>
      <span>888.555.0142</span>
    </div>
    <div class="contact" style="top:112px">
      <svg viewBox="0 0 28 28"><path d="M14 2a8 8 0 0 0-8 8c0 6 8 16 8 16s8-10 8-16a8 8 0 0 0-8-8zm0 11a3 3 0 1 1 0-6 3 3 0 0 1 0 6z" fill="var(--white)"/></svg>
      <span>4410 Harlow Ave. | Suite 210 Linden, VA 23000</span>
    </div>
    <div class="band-brand">Brinvaro<br>Consulting</div>
  </div>
</section>

</body>
</html>
```